Buch-/eBook-Cover für Darmtherapie für Frauen
Von Herzen Danke. Das design ist super geworden. Ich glaube ich war nicht so einfach mit meinen Änderungen. Schnelle Kommunikation. DAAANKE!!!! Ich bin so glücklich
Zielgruppe
Darmtherapie für Frauen,
Mamas und Frauen mit Kinderwunsch
Babys und Kinder
Entdecke die transformierende
Kraft der Darmtherapie!
Wie eine Darmtherapie dein Immunsystem ganzheitlich regulieren und dir bei hormonellem Ungleichgewicht helfen kann, ohne deinen Körper durch einen vermeidbaren Ärztemarathon zusätzlich zu belasten.
Ich begleite dich auf deinem Weg in ein erfülltes (Mama) – Leben.
Weil ganzheitliche Gesundheit im Darm beginnt.
Ich möchte nicht, dass dieses Buch ein weiteres ist, das du liest und dann wieder vergisst. Dieses Buch soll dich durch deine verschiedenen Lebensphasen begleiten. Du kannst dir die Informationen und Werkzeuge herausnehmen, die zu deiner Situation und deiner Familie passen.
In diesem Buch findest du freie Felder, leere Seiten und Aufgaben, in denen du deine Gedanken und Notizen festhalten kannst. Hier findest du auch Zitate, Rezepte, Übungen und Anleitungen, die speziell auf deine Lebensphase und die deiner Kinder zugeschnitten sind.
Aufgabenstellung
Eyecather Titel. Eyecather Cover. Eilt nicht Cover mit einem Heilstein oder so. Evtl Titel des Flyers mit einarbeiten: Entdecke die transformierende Kraft der Darmtherapie ( nur Vorschlag)
Es soll nicht der Flyer als Cover werden. Flyer dient nur der Firmen Farben etc
Richtiger eye Catcher Titel. Gern etwas provokativ

```html
<!DOCTYPE html>
<html lang="de">
<head>
<meta charset="utf-8">
<title>Darmtherapie – Buchumschlag</title>
<link href="https://fonts.googleapis.com/css2?family=Roboto:wght@400;500;700&display=swap" rel="stylesheet">
<style>
  :root {
    --teal: #7fbdc3;
    --teal-dark: #3c9c99;
    --olive: #c8c33d;
    --white: #ffffff;
    --stage: #b3b3b3;
    --ink-olive: #8f8b1e;
  }
  * { box-sizing: border-box; margin: 0; padding: 0; }
  html, body { width: 960px; height: 1200px; overflow: hidden; }
  body { background: var(--stage); font-family: 'Roboto', sans-serif; position: relative; }

  .spread {
    position: absolute; left: 20px; top: 280px;
    width: 920px; height: 640px; display: flex;
    box-shadow: 0 6px 18px rgba(0,0,0,.25);
  }
  .panel { position: relative; height: 100%; overflow: hidden; }
  .wave { position: absolute; left: 0; width: 100%; display: block; }

  /* Back cover */
  .back { width: 428px; background: var(--teal); }
  .back-kicker, .back-title {
    position: absolute; left: 0; width: 100%; text-align: center;
    color: var(--white); font-weight: 700; z-index: 2;
  }
  .back-kicker { top: 14px; font-size: 13px; letter-spacing: .4px; }
  .back-title { top: 38px; font-size: 18px; letter-spacing: .8px; }
  .info-box {
    position: absolute; left: 26px; width: 388px; border-radius: 10px;
    padding: 14px 10px 10px 10px; font-size: 9.6px; font-weight: 700;
    letter-spacing: .2px; line-height: 1.2;
  }
  .info-box h2 { font-size: 13.5px; font-weight: 700; letter-spacing: .4px; margin-bottom: 14px; }
  .info-box.olive { background: var(--olive); color: var(--white); }
  .info-box.light { background: var(--white); color: var(--teal-dark); }
  .info-box.light h2 { color: var(--teal-dark); }
  .why { top: 136px; height: 152px; }
  .who { top: 303px; height: 111px; padding-left: 14px; }
  .steps { top: 428px; height: 151px; padding-left: 20px; }
  .steps h2 { margin-top: 6px; }
  .steps ol { padding-left: 14px; }
  .steps li { margin-bottom: 2px; }
  .arrow { position: absolute; z-index: 3; }
  .back-footer {
    position: absolute; left: 0; top: 600px; width: 100%; text-align: center;
    color: var(--white); font-size: 9.5px; line-height: 1.3;
  }

  /* Spine */
  .spine { width: 65px; background: var(--olive); }
  .spine-mark {
    position: absolute; left: 13px; top: 228px; width: 40px; height: 40px;
    border-radius: 50%; background: var(--white);
  }
  .spine-text {
    position: absolute; left: 50%; top: 280px; transform-origin: 0 0;
    transform: rotate(90deg) translateY(-50%);
    white-space: nowrap; color: var(--white); font-weight: 500; letter-spacing: .6px;
  }
  .spine-text .line1 { font-size: 11px; display: block; }
  .spine-text .line2 { font-size: 14px; display: block; }

  /* Front cover */
  .front { width: 427px; background: var(--teal); }
  .brand {
    position: absolute; top: 14px; left: 0; width: 100%; z-index: 2;
    display: flex; justify-content: center; align-items: center; gap: 10px;
  }
  .brand-dot { width: 44px; height: 44px; border-radius: 50%; background: var(--olive); }
  .brand-name { color: var(--teal); font-weight: 500; font-size: 17px; letter-spacing: .8px; line-height: 1.05; }
  .front-title {
    position: absolute; top: 152px; left: 0; width: 100%; text-align: center;
    color: var(--white); font-weight: 700; font-size: 17.5px; line-height: 1.3; letter-spacing: .6px;
  }
  .front-body {
    position: absolute; top: 222px; left: 52px; width: 340px;
    color: var(--white); font-size: 13.2px; line-height: 1.3;
  }
  .front-body p { margin-bottom: 16px; }
  .front-footer {
    position: absolute; top: 592px; left: 0; width: 100%; text-align: center;
    color: var(--white); font-size: 11.5px; font-weight: 500; line-height: 1.4;
  }
</style>
</head>
<body>
<div class="spread">

  <section class="panel back">
    <svg class="wave" style="top:0" width="428" height="120" viewBox="0 0 428 120" preserveAspectRatio="none">
      <path d="M0 0H428V86C370 62 300 66 230 90C150 116 70 112 0 96Z" fill="#ffffff"/>
      <path d="M0 0H428V76C370 52 300 56 230 80C150 106 70 102 0 86Z" fill="#c8c33d"/>
    </svg>
    <p class="back-kicker">DARMTHERAPIE FÜR GANZHEITLICHE GESUNDHEIT!</p>
    <h1 class="back-title">DEIN WEG ZU MEHR WOHLBEFINDEN:</h1>

    <div class="info-box olive why">
      <h2>Warum eine Darmtherapie?</h2>
      <p>• Ein gesunder Darm ist der Schlüssel zu ganzheitlicher Gesundheit, einem intakten Immunsystem und mehr Lebensfreude<br>
      • Darmprobleme können den Menstruationszyklus und die natürliche Empfängnis beeinflussen. Die Darmtherapie kann hier korrigierend wirken<br>
      -Ein gesunder Darm bietet zahlreiche Vorteile, von besserer Nährstoffaufnahme bis zu gesteigerter Lebensqualität und Stimmung</p>
    </div>

    <svg class="arrow" style="left:330px;top:270px" width="50" height="60" viewBox="0 0 50 60">
      <path d="M14 2C40 8 44 36 12 52" fill="none" stroke="#222" stroke-width="1.6" stroke-dasharray="3 3"/>
      <path d="M18 46L10 53L19 56" fill="none" stroke="#222" stroke-width="1.6"/>
    </svg>

    <div class="info-box light who">
      <h2>Für wen ist die Darmtherapie geeignet?</h2>
      <p>• Frauen, die ihre ganzheitliche Gesundheit optimieren möchten<br>
      • Mütter auf der Suche nach mehr Energie und Wohlbefinden<br>
      • Frauen mit Kinderwunsch, um ihre Chancen zu erhöhen<br>
      -Babys und Kinder mit Verdauungsproblemen oder Hautirritationen</p>
    </div>

    <svg class="arrow" style="left:10px;top:400px" width="50" height="90" viewBox="0 0 50 90">
      <path d="M38 4C8 8 0 50 26 80" fill="none" stroke="#222" stroke-width="1.6" stroke-dasharray="3 3"/>
      <path d="M18 78L27 82L28 72" fill="none" stroke="#222" stroke-width="1.6"/>
    </svg>

    <div class="info-box olive steps">
      <h2>Das sind deine nächsten Schritte:</h2>
      <ol>
        <li>Kostenloses Beratungsgespräch: Sprechen wir über deine Bedürfnisse.</li>
        <li>Individuelle Therapie: Maßgeschneiderter Plan für deine ganzheitliche Gesundheit</li>
        <li>Nachhaltige Veränderung: Erfahre ein neues Lebensgefühl und gesteigerte Lebensqualität.</li>
      </ol>
    </div>

    <p class="back-footer">Mara Kurovest Holistische Darmtherapeutin, Lindenweg 12, 40210 Musterstadt,<br>
    Tel.: +49 0000 1234567, kontakt@sanftklar-kurovest.de</p>
  </section>

  <section class="panel spine">
    <div class="spine-mark"></div>
    <p class="spine-text"><span class="line1">SANFT &amp; KLAR</span><span class="line2">MARA KUROVEST</span></p>
  </section>

  <section class="panel front">
    <svg class="wave" style="top:0" width="427" height="130" viewBox="0 0 427 130" preserveAspectRatio="none">
      <path d="M0 0H427V110C400 80 370 62 320 64C250 66 190 110 120 110C70 110 30 90 0 70Z" fill="#ffffff"/>
    </svg>
    <div class="brand">
      <span class="brand-dot"></span>
      <span class="brand-name">SANFT &amp; KLAR<br>MARA KUROVEST</span>
    </div>

    <h1 class="front-title">ENTDECKE DIE TRANSFORMIERENDE<br>KRAFT DER DARMTHERAPIE!</h1>

    <div class="front-body">
      <p>Die ganzheitliche Darmtherapie ist speziell für Frauen, Mamas, und Frauen mit Kinderwunsch entwickelt- inklusive Babys und Kleinkinder!</p>
      <p>Erfahre, wie eine gesunde Darmflora<br>dein Immunsystem stärkt,<br>deinen Hormonhaushalt ausbalanciert und dich zu neuer Vitalität führt – ohne langwierige Arztbesuche.</p>
      <p>Ich begleite dich auf dem Weg zu einem erfüllten (Mama)-Leben, denn wahre Gesundheit beginnt im Darm.</p>
      <p>Auch deine Kleinsten sind willkommen!</p>
    </div>

    <svg class="wave" style="top:500px" width="427" height="140" viewBox="0 0 427 140" preserveAspectRatio="none">
      <path d="M0 22C60 0 130 0 200 24C270 48 350 50 427 14V140H0Z" fill="#ffffff"/>
      <path d="M0 40C60 14 130 12 200 36C270 60 350 60 427 20V140H0Z" fill="#c8c33d"/>
    </svg>
    <p class="front-footer">Jetzt dein kostenloses Beratungsgespräch vereinbaren.<br>www.sanftklar-kurovest.de</p>
  </section>

</div>
</body>
</html>
```